IT Business Card Design

My company is a newly started small IT repair business. I operate outside of usual hours except for Saturday.
I am a very experienced and professional Technician.
I would like the business card to express that I am running a professional business and not some home IT business. This should be expressed through the design of the business card.
On the back of the card I would like the name of the company to be displayed.
Updates
Sorry guys, I have updated the requirement to be double sided. Fantastic submissions so far! Keep up the good work.
Hey designers!
Hey Designers!
Thank you all for your hard work!
Target Market(s)
Home to small business users.
Industry/Entity Type
Business
Contact Information for Business Card
Harbourlight Technics
Marcus Pendleby (Director)
marcus.pendleby@quorvanet.com.au
Operating Hours
5pm-12am Mon - Fri
9am - 5pm Sat
Mobile
0417962351
Requirements
Must have
- The base colour must be matte black. There must be some dark purple. (To go with the "Harbourlight" theme)

```html
<!DOCTYPE html>
<html lang="en">
<head>
<meta charset="utf-8">
<title>Harbourlight Technics – Business Card Back</title>
<link rel="stylesheet" href="https://fonts.googleapis.com/css2?family=Michroma&display=swap">
<style>
  :root {
    --canvas-bg: #ffffff;
    --card-edge: #2b2fd6;
    --night-base: #03041a;
    --deep-navy: #070a3a;
    --electric-blue: #2a22e0;
    --royal-violet: #5a1ff0;
    --neon-magenta: #b046f2;
    --glow-white: #f4e9ff;
    --title-white: #ffffff;
    --title-shadow: #05051a;
  }

  * { margin: 0; padding: 0; box-sizing: border-box; }

  html, body {
    width: 1200px;
    height: 740px;
    overflow: hidden;
    background: var(--canvas-bg);
  }

  .card-back {
    position: relative;
    width: 1200px;
    height: 740px;
    overflow: hidden;
    background: var(--night-base);
    border: 2px solid var(--card-edge);
  }

  .glow-artwork {
    position: absolute;
    inset: 0;
    background:
      radial-gradient(circle at 50% 47%,
        var(--royal-violet) 0%,
        var(--electric-blue) 7%,
        var(--neon-magenta) 20%,
        var(--royal-violet) 32%,
        var(--electric-blue) 42%,
        var(--deep-navy) 58%,
        var(--night-base) 78%);
  }

  .company-title {
    position: absolute;
    left: 0;
    right: 0;
    top: 208px;
    text-align: center;
    font-family: "Michroma", "Arial Black", sans-serif;
    font-size: 52px;
    font-variant: small-caps;
    letter-spacing: 4px;
    color: var(--title-white);
    text-shadow: 4px 4px 0 var(--title-shadow);
    white-space: nowrap;
  }
</style>
</head>
<body>
  <main class="card-back">
    <div class="glow-artwork" role="img" aria-label="Abstract glowing violet and blue concentric light rings with diagonal light streaks on a dark night background"></div>
    <h1 class="company-title">Harbourlight Technics</h1>
  </main>
</body>
</html>
```